Design a "healthy, happy dog and cat" cheque/check background

I am looking for a few design concepts featuring a happy healthy dog and cat, that will be used as the background of a paper cheque/check.

This will require Photoshop and stock photos.

Here is the design brief: https://files.brivontel.net/sheet/48kQmZ2xTrWvLpN7aHcYeJ5uBdFsKo9GiRtXnVw3Lz/view?share=on

Colors

Designer to choose colors to be used in the design.

Requirements
Must have
• A happy dog and cat the main focus within the "empty" central part of the cheque/check, and a complementary background for the rest of the cheque, following the design guidelines in the attached google doc.

```html
<!DOCTYPE html>
<html lang="en">
<head>
<meta charset="utf-8">
<title>Personal Cheque – Dog and Cat</title>
<link rel="stylesheet" href="https://fonts.googleapis.com/css2?family=Arimo:wght@400;700&family=Share+Tech+Mono&display=swap">
<style>
  :root {
    --paper: #ffffff;
    --ink: #1a1a1a;
    --ink-soft: #444444;
    --rule: #333333;
    --micr: #5a6068;
    --pet-light: #f6e7d3;
    --pet-mid: #e9c9a0;
    --pet-deep: #d7a871;
    --badge: #8a8a8a;
  }
  * { margin: 0; padding: 0; box-sizing: border-box; }
  html, body {
    width: 1200px; height: 544px; overflow: hidden;
    background: var(--paper);
  }
  .cheque {
    position: relative; width: 1200px; height: 544px;
    background: var(--paper);
    font-family: "Arimo", Arial, sans-serif;
    color: var(--ink);
  }
  .pet-photo {
    position: absolute; left: 318px; top: 34px; width: 556px; height: 440px;
    border-radius: 46% 46% 18% 18% / 40% 40% 12% 12%;
    background:
      radial-gradient(ellipse at 30% 45%, var(--pet-mid) 0%, rgba(233,201,160,0.55) 40%, rgba(246,231,211,0) 72%),
      radial-gradient(ellipse at 72% 48%, var(--pet-deep) 0%, rgba(215,168,113,0.5) 38%, rgba(246,231,211,0) 70%);
    opacity: 0.75;
  }
  .account-holder { position: absolute; left: 58px; top: 60px; line-height: 20px; }
  .account-holder__name { font-size: 21px; font-weight: 700; color: var(--ink-soft); line-height: 24px; }
  .account-holder__line { font-size: 20px; color: var(--ink-soft); }
  .cheque-number { position: absolute; left: 1023px; top: 46px; font-size: 24px; font-weight: 700; }
  .date-label { position: absolute; left: 784px; top: 110px; font-size: 20px; color: var(--ink-soft); }
  .date-format {
    position: absolute; left: 866px; top: 131px; display: flex; gap: 25px;
    font-size: 14px; color: var(--ink);
  }
  .payee-label { position: absolute; left: 56px; top: 190px; font-size: 14px; line-height: 14px; }
  .currency { position: absolute; left: 947px; top: 186px; font-size: 28px; color: var(--ink-soft); }
  .amount-words { position: absolute; left: 918px; top: 253px; font-size: 15px; }
  .rules { position: absolute; inset: 0; }
  .institution { position: absolute; left: 58px; top: 290px; display: flex; gap: 8px; }
  .institution__mark { width: 80px; height: 80px; border-radius: 50%; background: var(--ink); margin-top: -2px; }
  .institution__text { font-size: 19px; line-height: 19px; padding-top: 6px; }
  .institution__name { font-weight: 700; }
  .company-name { position: absolute; left: 808px; top: 333px; font-size: 14px; }
  .memo-label { position: absolute; left: 60px; top: 384px; font-size: 12px; color: var(--ink-soft); }
  .micr-line {
    position: absolute; left: 54px; top: 448px;
    font-family: "Share Tech Mono", monospace; font-size: 30px; letter-spacing: 3px;
    color: var(--micr);
  }
  .security-badge { position: absolute; left: 1160px; top: 272px; }
</style>
</head>
<body>
<main class="cheque">
  <div class="pet-photo" role="img" aria-label="Photo of a ginger kitten sitting beside a golden long-haired puppy, softly faded into the cheque"></div>

  <div class="account-holder">
    <p class="account-holder__name">Northmere Cheques Personal Cheque</p>
    <p class="account-holder__line">27 Maplecrest Lane</p>
    <p class="account-holder__line">Riverton, Ontario K2K 2K2</p>
  </div>

  <p class="cheque-number">101</p>
  <p class="date-label">DATE</p>
  <div class="date-format"><span>D</span><span>D</span><span>M</span><span>M</span><span>Y</span><span>Y</span><span>Y</span><span>Y</span></div>

  <p class="payee-label">PAY TO THE<br>ORDER OF</p>
  <p class="currency">$</p>
  <p class="amount-words">100 DOLLARS</p>

  <svg class="rules" width="1200" height="544" viewBox="0 0 1200 544" aria-hidden="true">
    <g stroke="var(--rule)" stroke-width="1.4" fill="none">
      <polyline points="56,221 922,221 922,190"/>
      <polyline points="56,277 905,277 912,240"/>
      <line x1="60" y1="397" x2="586" y2="397"/>
      <line x1="686" y1="397" x2="1098" y2="397"/>
    </g>
  </svg>

  <div class="institution">
    <div class="institution__mark"></div>
    <div class="institution__text">
      <p class="institution__name">Your Financial Institution</p>
      <p>200 Finance Avenue</p>
      <p>Your City, Your Province A1B 2CS</p>
    </div>
  </div>

  <p class="company-name">Optional Company Name</p>
  <p class="memo-label">MEMO</p>

  <p class="micr-line">⑈101⑈ ⑆12345⑉678⑆ 12345⑉6789⑈</p>

  <svg class="security-badge" width="32" height="134" viewBox="0 0 32 134" aria-hidden="true">
    <rect x="1" y="1" width="30" height="132" rx="3" fill="none" stroke="var(--badge)" stroke-width="1" stroke-dasharray="3 2"/>
  </svg>
</main>
</body>
</html>
```